Medical Billing - Professional Marketing Flier

We are needing help designing a clean and professional looking easy to read marketing flier for a medical billing practice. The text needs to be large enough to print. We are looking for a 5.5 x 8.5 design that we can edit the text as needed. I have included our logo and what we initially want it to say. Please keep in mind, we also want our logo and contact details on the flier. Let me know if you have any questions.

```html
<!DOCTYPE html>
<html lang="en">
<head>
<meta charset="utf-8">
<title>Vega Medical Billing – Flier</title>
<link href="https://fonts.googleapis.com/css2?family=Montserrat:wght@500;600;700;800&display=swap" rel="stylesheet">
<style>
  :root {
    --board: #c9c9c9;
    --navy: #0d1f55;
    --white: #ffffff;
    --purple: #7b5cb8;
    --pink: #e05fa8;
    --brand: #7a4fb0;
    --ink: #4a4a55;
  }
  * { margin: 0; padding: 0; box-sizing: border-box; }
  html, body { width: 1200px; height: 2629px; overflow: hidden; }
  body {
    background: var(--board);
    font-family: "Montserrat", sans-serif;
    position: relative;
  }
  .flier {
    position: absolute;
    left: 227px;
    width: 749px;
    height: 1112px;
    background: var(--navy);
    overflow: hidden;
    box-shadow: 0 10px 18px rgba(0,0,0,0.28);
  }
  .flier--front { top: 136px; }
  .flier--back { top: 1350px; }

  .hero-curve { position: absolute; left: 0; top: 0; }

  .brand {
    position: absolute;
    text-align: center;
    color: var(--brand);
    font-family: "Montserrat", sans-serif;
    font-weight: 600;
    line-height: 1;
  }
  .brand__name { display: block; font-size: 82px; letter-spacing: 4px; }
  .brand__tag { display: block; font-size: 19px; letter-spacing: 5px; margin-top: 8px; }
  .flier--front .brand { left: 0; width: 749px; top: 150px; }
  .flier--back .brand { left: 60px; width: 290px; top: 100px; }
  .flier--back .brand__name { font-size: 64px; }
  .flier--back .brand__tag { font-size: 15px; letter-spacing: 4px; }

  .photo {
    position: absolute;
    left: 0; top: 0;
    width: 749px; height: 405px;
    background: linear-gradient(100deg, #b7c7a0 0%, #e7ece6 22%, #f4f6f8 50%, #dfe4ea 78%, #f1f3f6 100%);
  }
  .photo-rule {
    position: absolute;
    left: 0; top: 405px;
    width: 749px; height: 7px;
    background: linear-gradient(90deg, var(--purple), var(--pink), var(--purple));
  }

  .section {
    position: absolute;
    left: 28px;
    width: 694px;
    color: var(--white);
  }
  .section__title {
    font-weight: 700;
    font-size: 31px;
    letter-spacing: 0.3px;
    padding-left: 4px;
    line-height: 1;
  }
  .section__title::after {
    content: "";
    display: block;
    width: 92px; height: 3px;
    margin-top: 8px;
    background: linear-gradient(90deg, var(--pink), var(--purple));
  }
  .section__body {
    margin-top: 18px;
    font-weight: 500;
    font-size: 19.4px;
    line-height: 27.8px;
    text-align: justify;
  }

  .contact-bar {
    position: absolute;
    left: 0; top: 1033px;
    width: 749px; height: 79px;
    background: var(--white);
  }
  .contact-bar__tab { position: absolute; left: 0; top: 0; }
  .contact-bar__label {
    position: absolute;
    left: 26px; top: 22px;
    font-weight: 800;
    font-size: 30px;
    letter-spacing: 0.5px;
    line-height: 1;
  }
  .flier--front .contact-bar__label { color: var(--navy); }
  .flier--back .contact-bar__label { color: var(--white); }
  .contact-list {
    position: absolute;
    left: 393px; top: 8px;
    list-style: none;
    color: var(--ink);
    font-weight: 500;
    font-size: 17.5px;
    line-height: 21.5px;
  }
  .contact-list li { display: flex; align-items: center; gap: 5px; }
  .contact-list svg { flex: none; }
</style>
</head>
<body>

<svg width="0" height="0" style="position:absolute">
  <defs>
    <linearGradient id="arc-grad" x1="0" y1="0" x2="1" y2="0">
      <stop offset="0" stop-color="#7b5cb8"/>
      <stop offset="0.7" stop-color="#e05fa8"/>
      <stop offset="1" stop-color="#9b5fc0"/>
    </linearGradient>
    <linearGradient id="tab-grad" x1="0" y1="0" x2="1" y2="0">
      <stop offset="0" stop-color="#b35cb4"/>
      <stop offset="0.35" stop-color="#e05fa8"/>
      <stop offset="1" stop-color="#7b5cb8"/>
    </linearGradient>
  </defs>
</svg>

<!-- Front page -->
<article class="flier flier--front">
  <svg class="hero-curve" width="749" height="400" viewBox="0 0 749 400">
    <path d="M0,170 C250,480 620,470 749,58 V220 C600,390 250,420 0,170 Z" fill="url(#arc-grad)"/>
    <path d="M0,0 H749 V220 C600,390 250,420 0,170 Z" fill="#ffffff"/>
  </svg>

  <div class="brand">
    <span class="brand__name">VEGA</span>
    <span class="brand__tag">MEDICAL BILLING</span>
  </div>

  <section class="section" style="top:440px">
    <h2 class="section__title">MEDICAL BILLING</h2>
    <p class="section__body">Would you prefer to spend time focusing on your clients and running your practice rather than trying to stay up to speed with the constantly changing medical billing rules and regulations? Let us help you by managing your medical billing and dealing with the insurance companies on your behalf! We work with you to tailor the entire medical billing process to suit your practices needs while making it as smooth and painless as possible.</p>
  </section>

  <section class="section" style="top:729px">
    <h2 class="section__title">AGING</h2>
    <p class="section__body">Are you leaving money on the table? Are you able to do the follow-through needed to keep your aging in check and more money flowing into your practice? Are you uncertain about how to get insurance to pay on claims that should be covered but for some reason they decided not to? We can clean up your aging, reduce the amount of time it takes for claims to pay out, and we can keep your aging to a minimum.</p>
  </section>

  <footer class="contact-bar">
    <svg class="contact-bar__tab" width="310" height="79" viewBox="0 0 310 79">
      <path d="M0,0 H284 L236,79 H0 Z" fill="url(#tab-grad)"/>
      <path d="M300,0 L252,79" stroke="#7b5cb8" stroke-width="3"/>
    </svg>
    <span class="contact-bar__label">CONTACT US</span>
    <ul class="contact-list">
      <li><svg width="13" height="13" viewBox="0 0 24 24"><path d="M6.6 10.8a15 15 0 0 0 6.6 6.6l2.2-2.2a1 1 0 0 1 1-.25 11.4 11.4 0 0 0 3.6.57 1 1 0 0 1 1 1V20a1 1 0 0 1-1 1A17 17 0 0 1 3 4a1 1 0 0 1 1-1h3.5a1 1 0 0 1 1 1c0 1.25.2 2.45.57 3.6a1 1 0 0 1-.25 1z" fill="#8a5cc0"/></svg>555-014-2287</li>
      <li><svg width="13" height="13" viewBox="0 0 24 24"><circle cx="12" cy="12" r="10" fill="none" stroke="#8a5cc0" stroke-width="2.4"/><path d="M2 12h20M12 2c3 3 3 17 0 20M12 2c-3 3-3 17 0 20" fill="none" stroke="#8a5cc0" stroke-width="2"/></svg>www.vegamedicalbilling.com</li>
      <li><svg width="13" height="13" viewBox="0 0 24 24"><rect x="2" y="5" width="20" height="14" fill="#8a5cc0"/><path d="M2 5l10 8 10-8" fill="none" stroke="#fff" stroke-width="1.8"/></svg>admin@vegamedicalbilling.com</li>
    </ul>
  </footer>
</article>

<!-- Back page -->
<article class="flier flier--back">
  <div class="photo" role="img" aria-label="Photo of a stethoscope resting on paperwork on a bright office desk with a keyboard and a green plant"></div>
  <div class="photo-rule"></div>

  <div class="brand">
    <span class="brand__name">VEGA</span>
    <span class="brand__tag">MEDICAL BILLING</span>
  </div>

  <section class="section" style="top:508px; left:25px">
    <h2 class="section__title">CREDENTIALING</h2>
    <p class="section__body">Are you wanting to get contracted with insurance companies but aren’t sure how to go about it? Are you wanting to expand your client base by having the option to bill insurance? Let us take the confusion out of what can seem like a daunting task! We can get you and your practitioners contracted with the insurance companies of your choice and help you navigate through the process every step of the way!</p>
  </section>

  <section class="section" style="top:780px; left:25px">
    <h2 class="section__title">CONTACT US</h2>
    <p class="section__body">If any of these processes are something you would like our help with or to consult with us on, please email us or give us a call! We specialize in billing and contracting for Nutritionists and Dietitians. We would love to help you expand your business and take the pain and frustration out of billing so you can focus on your clients.</p>
  </section>

  <footer class="contact-bar">
    <svg class="contact-bar__tab" width="310" height="79" viewBox="0 0 310 79">
      <path d="M0,0 H284 L236,79 H0 Z" fill="url(#tab-grad)"/>
      <path d="M300,0 L252,79" stroke="#7b5cb8" stroke-width="3"/>
    </svg>
    <span class="contact-bar__label">CONTACT US</span>
    <ul class="contact-list">
      <li><svg width="13" height="13" viewBox="0 0 24 24"><path d="M6.6 10.8a15 15 0 0 0 6.6 6.6l2.2-2.2a1 1 0 0 1 1-.25 11.4 11.4 0 0 0 3.6.57 1 1 0 0 1 1 1V20a1 1 0 0 1-1 1A17 17 0 0 1 3 4a1 1 0 0 1 1-1h3.5a1 1 0 0 1 1 1c0 1.25.2 2.45.57 3.6a1 1 0 0 1-.25 1z" fill="#8a5cc0"/></svg>555-014-2287</li>
      <li><svg width="13" height="13" viewBox="0 0 24 24"><circle cx="12" cy="12" r="10" fill="none" stroke="#8a5cc0" stroke-width="2.4"/><path d="M2 12h20M12 2c3 3 3 17 0 20M12 2c-3 3-3 17 0 20" fill="none" stroke="#8a5cc0" stroke-width="2"/></svg>www.vegamedicalbilling.com</li>
      <li><svg width="13" height="13" viewBox="0 0 24 24"><rect x="2" y="5" width="20" height="14" fill="#8a5cc0"/><path d="M2 5l10 8 10-8" fill="none" stroke="#fff" stroke-width="1.8"/></svg>admin@vegamedicalbilling.com</li>
    </ul>
  </footer>
</article>

</body>
</html>
```